copper ridge construction website (squarespace build)

construction website - see attached documents

Target Market(s)

owners, cm's, and gc's

Coding

Coded - Design and coding required

Font styles to use
Serif

Colors
0054AA
0677BA
7BADD7
CADEEF
E8F1F8

```html
<!DOCTYPE html>
<html lang="en">
<head>
<meta charset="utf-8">
<title>Copper Ridge Construction</title>
<link href="https://fonts.googleapis.com/css2?family=Playfair+Display:wght@400;500&family=Roboto+Condensed:wght@300;400;600;700&family=Poppins:wght@400;500;600&display=swap" rel="stylesheet">
<style>
:root{
  --navy:#04193d;
  --navy-deep:#031431;
  --blue:#0054AA;
  --blue-mid:#0677BA;
  --blue-soft:#7BADD7;
  --blue-pale:#CADEEF;
  --blue-wash:#E8F1F8;
  --ink:#1b1f27;
  --text:#3d4450;
  --white:#ffffff;
}
*{box-sizing:border-box;margin:0;padding:0}
html,body{width:1200px;height:5000px;overflow:hidden}
body{font-family:"Poppins",sans-serif;color:var(--text);background:var(--white);position:relative}
section,header,footer{position:absolute;left:0;width:1200px}
.abs{position:absolute}

/* header */
.site-header{top:0;height:76px;background:var(--white)}
.brand{left:142px;top:18px;height:38px;display:flex;align-items:center;gap:8px;font-family:"Roboto Condensed",sans-serif;font-weight:700;font-size:24px;color:var(--navy);letter-spacing:.5px}
.brand-mark{width:16px;height:16px;background:var(--blue)}
.nav{right:142px;top:22px;display:flex;align-items:center;gap:22px;font-size:12px;font-weight:500;color:var(--navy)}
.nav .active{color:var(--blue-mid)}
.nav-contact{display:flex;align-items:center;border:1px solid var(--navy);height:34px}
.nav-contact .ico{width:34px;height:34px;background:var(--navy);display:flex;align-items:center;justify-content:center}
.nav-contact span{padding:0 16px}

/* hero */
.hero{top:76px;height:549px;background:linear-gradient(90deg,#0c2450 0%,#1a3c6c 45%,#6d7561 80%,#8a7a52 100%)}
.hero-photo{position:absolute;inset:0;background:linear-gradient(90deg,rgba(4,25,61,.92) 0%,rgba(4,25,61,.55) 50%,rgba(4,25,61,.05) 100%)}
.hero-title{left:142px;top:52px;font-family:"Playfair Display",serif;font-weight:400;font-size:58px;line-height:69px;color:var(--white);text-transform:uppercase;white-space:nowrap}
.hero-tags{left:142px;top:266px;font-weight:600;font-size:18px;color:var(--blue-soft);letter-spacing:.3px}
.hero-lede{left:142px;top:302px;width:450px;padding-left:12px;border-left:2px solid var(--white);font-size:14px;line-height:25px;color:var(--white)}
.hero-btn{left:142px;top:390px;height:42px;display:flex;background:var(--white)}
.hero-btn .ico{width:46px;background:var(--blue);display:flex;align-items:center;justify-content:center}
.hero-btn span{padding:0 20px;line-height:42px;font-weight:600;font-size:15px;color:var(--blue)}
.hero-bar{left:0;top:487px;width:1200px;height:62px;background:rgba(4,25,61,.85);display:flex;align-items:center;padding-left:142px;gap:48px}
.badge{display:flex;align-items:center;gap:12px;color:var(--blue-pale);font-size:14px;line-height:17px;text-transform:uppercase}

/* about */
.about{top:625px;height:765px;background:var(--white)}
.about-frame{left:107px;top:146px;width:343px;height:520px;border:2px solid var(--blue-mid)}
.about-photo{left:142px;top:97px;width:435px;height:540px;background:linear-gradient(160deg,#8fb4d6 0%,#7a8b86 40%,#6b4e3a 75%,#8a7358 100%)}
.about-seal{left:518px;top:300px;width:100px;height:100px;border-radius:50%;background:var(--blue);border:4px solid var(--white)}
.eyebrow{display:flex;align-items:center;gap:10px;font-family:"Roboto Condensed",sans-serif;font-weight:600;font-size:13px;color:var(--blue-mid);text-transform:uppercase}
.eyebrow::before{content:"";width:28px;height:2px;background:var(--blue-mid)}
.eyebrow.center::after{content:"";width:28px;height:2px;background:var(--blue-mid)}
.h2{font-family:"Roboto Condensed",sans-serif;font-weight:300;color:var(--ink);text-transform:uppercase;font-size:40px;line-height:44px;white-space:nowrap}
.h2 b{font-weight:700}
.about-text{left:643px;top:107px;width:405px}
.about-text .h2{margin-top:10px;font-size:38px}
.about-text p{font-size:12.5px;line-height:19.5px;margin-top:18px}
.about-text p:first-of-type{margin-top:22px}
.btn-row{display:flex;gap:16px;margin-top:30px}
.btn{height:40px;padding:0 14px;line-height:38px;font-family:"Roboto Condensed",sans-serif;font-weight:600;font-size:13px;text-transform:uppercase}
.btn-outline{border:1px solid var(--ink);color:var(--ink)}
.btn-solid{background:var(--blue-mid);color:var(--white);border:1px solid var(--blue-mid);padding:0 22px}

/* services */
.services{top:1390px;height:591px;background:var(--blue-wash);text-align:center}
.sec-head{position:absolute;left:0;width:1200px;display:flex;flex-direction:column;align-items:center}
.sec-head .h2{margin-top:8px}
.sec-head p{font-size:13px;line-height:20px;margin-top:10px;color:var(--text)}
.svc{position:absolute;width:418px;height:109px;background:var(--white);text-align:left;padding:22px 30px 0 56px;box-shadow:0 4px 14px rgba(4,25,61,.05)}
.svc.right{padding:22px 56px 0 30px}
.svc h3{font-family:"Roboto Condensed",sans-serif;font-weight:700;font-size:16px;color:var(--ink);text-transform:uppercase}
.svc p{font-size:11.5px;line-height:18px;margin-top:6px}
.svc-ico{position:absolute;width:58px;height:58px;display:flex;align-items:center;justify-content:center}
.bg-blue{background:var(--blue-mid)}
.bg-navy{background:var(--navy)}

/* why */
.why{top:1981px;height:538px;background:var(--navy)}
.why-edge{left:0;top:0;width:86px;height:538px;background:var(--blue-mid)}
.why-photo{left:600px;top:0;width:600px;height:538px;background:linear-gradient(180deg,#9aa3a4 0%,#9c7b56 40%,#a27a54 70%,#8b6a4b 100%)}
.why-text{left:142px;top:90px;width:410px}
.why-text .h2{color:var(--white);margin-top:8px}
.why-text p{font-size:12.5px;line-height:20px;color:var(--white);margin-top:16px}

/* projects */
.projects{top:2519px;height:1146px;background:var(--white)}
.proj{position:absolute;width:450px;height:393px;overflow:hidden}
.proj-shade{position:absolute;inset:0;background:linear-gradient(180deg,rgba(4,25,61,0) 55%,rgba(4,25,61,.9) 100%)}
.proj-cap{position:absolute;left:18px;bottom:20px;color:var(--white);font-family:"Roboto Condensed",sans-serif;text-transform:uppercase}
.proj-cap small{display:block;font-weight:600;font-size:14px}
.proj-cap strong{display:block;font-weight:700;font-size:29px;line-height:34px}
.proj-arrow{position:absolute;right:16px;bottom:18px;width:34px;height:34px;border:1px solid var(--white);display:flex;align-items:center;justify-content:center}

/* markets */
.markets{top:3665px;height:615px;background:var(--blue-wash)}
.mkt{position:absolute;top:303px;width:163px;height:221px;background:var(--white);padding:22px 18px 0 22px;box-shadow:0 4px 14px rgba(4,25,61,.06)}
.mkt-ico{width:40px;height:40px;background:var(--blue);display:flex;align-items:center;justify-content:center}
.mkt h4{font-family:"Roboto Condensed",sans-serif;font-weight:700;font-size:14px;line-height:17px;color:var(--ink);text-transform:uppercase;margin-top:22px}
.mkt p{font-size:11px;line-height:18px;margin-top:6px}

/* cta + footer */
.site-footer{top:4280px;height:720px;background:var(--navy)}
.cta{left:142px;top:93px;width:916px;height:230px;background:var(--blue)}
.cta-photo{left:751px;top:22px;width:165px;height:301px;background:linear-gradient(180deg,#e0b33a 0%,#2c3f73 40%,#22335f 100%);border-radius:80px 80px 0 0}
.cta-title{left:208px;top:138px;font-family:"Roboto Condensed",sans-serif;font-weight:300;font-size:40px;line-height:44px;color:var(--white);text-transform:uppercase;white-space:nowrap}
.cta-title b{font-weight:700}
.cta-sub{left:208px;top:240px;width:470px;font-size:12px;line-height:19px;color:var(--blue-pale)}
.cta-btn{left:759px;width:130px;height:43px;line-height:41px;text-align:center;font-family:"Roboto Condensed",sans-serif;font-weight:600;font-size:13px;text-transform:uppercase}
.cta-btn.ghost{top:157px;border:1px solid var(--white);color:var(--white)}
.cta-btn.fill{top:216px;background:var(--white);color:var(--blue)}
.fcol{top:416px}
.fcol h5{font-family:"Roboto Condensed",sans-serif;font-weight:600;font-size:16px;color:var(--white);text-transform:uppercase;padding-bottom:6px;border-bottom:2px solid var(--blue-mid);display:inline-block}
.fcol ul{list-style:none;margin-top:26px}
.fcol li{font-size:12.5px;line-height:27px;color:var(--white)}
.contact-item{display:flex;gap:8px;font-size:12px;line-height:20px;color:var(--white);margin-top:10px}
.contact-item:first-of-type{margin-top:26px}
.social li{display:flex;align-items:center;gap:10px;line-height:42px}
.social .dot{width:28px;height:28px;border-radius:50%;border:1px solid var(--white)}
.social .dot.on{background:var(--blue-mid);border-color:var(--blue-mid)}
.foot-rule{left:142px;top:662px;width:916px;height:1px;background:rgba(202,222,239,.2)}
.copyright{left:0;top:684px;width:1200px;text-align:center;font-size:12px;color:var(--white)}
</style>
</head>
<body>

<header class="site-header">
  <div class="abs brand"><span class="brand-mark"></span>COPPER RIDGE</div>
  <nav class="abs nav">
    <span class="active">HOME</span><span>ABOUT</span><span>SERVICES</span><span>PORTFOLIO</span><span>MARKETS &amp; INDUSTRIES</span>
    <div class="nav-contact"><div class="ico"><svg width="16" height="16" viewBox="0 0 24 24"><path fill="#fff" d="M6.6 10.8a15.1 15.1 0 006.6 6.6l2.2-2.2c.3-.3.7-.4 1-.2 1.1.4 2.3.6 3.6.6.6 0 1 .4 1 1V20c0 .6-.4 1-1 1A17 17 0 013 4c0-.6.4-1 1-1h3.5c.6 0 1 .4 1 1 0 1.3.2 2.5.6 3.6.1.3 0 .7-.2 1z"/></svg></div><span>CONTACT</span></div>
  </nav>
</header>

<section class="hero">
  <div class="hero-photo" role="img" aria-label="Workers in safety vests beside a drilling rig on a foundation site with a city skyline behind"></div>
  <h1 class="abs hero-title">The Quality<br>Starts at the<br>Foundation</h1>
  <div class="abs hero-tags">SAFETY | QUALITY | EXPERIENCE | CRAFTSMEN</div>
  <p class="abs hero-lede">Copper Ridge Construction is a self-performing foundation and geotechnical general contractor delivering precision.</p>
  <div class="abs hero-btn"><div class="ico"><svg width="20" height="20" viewBox="0 0 20 20"><path d="M4 4l6 6-6 6M10 4l6 6-6 6" stroke="#fff" stroke-width="2" fill="none"/></svg></div><span>VIEW OUR CORE SERVICES</span></div>
  <div class="abs hero-bar">
    <div class="badge"><svg width="28" height="28" viewBox="0 0 24 24" fill="none" stroke="#CADEEF" stroke-width="1.5"><path d="M12 3l8 3v6c0 5-3.5 8-8 9-4.5-1-8-4-8-9V6z"/><path d="M8.5 12l2.5 2.5 4.5-5"/></svg>Industry<br>Experts</div>
    <div class="badge"><svg width="28" height="28" viewBox="0 0 24 24" fill="none" stroke="#CADEEF" stroke-width="1.5"><rect x="4" y="3" width="16" height="18" rx="1"/><path d="M8 8h8M8 12h8M8 16h5"/></svg>Licensed &amp;<br>Insured</div>
    <div class="badge"><svg width="28" height="28" viewBox="0 0 24 24" fill="none" stroke="#CADEEF" stroke-width="1.5"><circle cx="12" cy="12" r="3.5"/><path d="M12 2v3M12 19v3M2 12h3M19 12h3M4.9 4.9l2.1 2.1M17 17l2.1 2.1M4.9 19.1L7 17M17 7l2.1-2.1"/></svg>Self<br>Performing</div>
  </div>
</section>

<section class="about">
  <div class="abs about-frame"></div>
  <div class="abs about-photo" role="img" aria-label="Red foundation drilling rig on an urban job site beside apartment buildings"></div>
  <div class="abs about-seal"></div>
  <div class="abs about-text">
    <div class="eyebrow">About Us</div>
    <h2 class="h2">The Strength of Every<br>Project <b>Begins Below<br>the Surface.</b></h2>
    <p>Copper Ridge Construction is a self-performing foundation and geotechnical general contractor and the critical first phase of every successful project.</p>
    <p>Copper Ridge partners with owners, construction managers, and general contractors from design through construction delivery. Our team supports projects at every phase — preconstruction, engineering and design support, exploratory investigations, design proof testing, and complete structural packages for our clients. Copper Ridge brings precision, accountability, and true partnership to ground-level work — because what's below the surface determines everything above it.</p>
    <p>Our projects managed and built by experienced professionals and skilled craftsmen, we hold safety and quality to the...</p>
    <div class="btn-row"><span class="btn btn-outline">Read More</span><span class="btn btn-solid">Request a Consultation</span></div>
  </div>
</section>

<section class="services">
  <div class="sec-head" style="top:90px">
    <div class="eyebrow center">Our Services</div>
    <h2 class="h2">Complete <b>Foundation Solutions</b></h2>
    <p>From deep foundations to earth retention and structural concrete, Copper Ridge delivers fully integrated site solutions<br>with self-performing crews and engineering-driven execution.</p>
  </div>
  <div class="svc" style="left:165px;top:249px"><h3>Owner, CM's, and GC's Services</h3><p>Complete Turnkey Site &amp; Structural Packages, Site Constructability And Logistical Assessments...</p></div>
  <div class="svc-ico bg-blue" style="left:142px;top:274px"><svg width="26" height="26" viewBox="0 0 24 24" fill="#fff"><circle cx="12" cy="8" r="4"/><path d="M4 21c0-4.4 3.6-7 8-7s8 2.6 8 7z"/></svg></div>
  <div class="svc right" style="left:616px;top:249px"><h3>Foundation &amp; Earth Retention</h3><p>Foundation &amp; Excavation, Driven &amp; Drilled Pile Systems, Helical Piles, Auger Cast Piles...</p></div>
  <div class="svc-ico bg-navy" style="left:1000px;top:274px"><svg width="28" height="28" viewBox="0 0 24 24" fill="none" stroke="#fff" stroke-width="1.8"><circle cx="12" cy="12" r="9"/><path d="M3 12h18M12 3c3 3 3 15 0 18M12 3c-3 3-3 15 0 18"/></svg></div>
  <div class="svc" style="left:165px;top:391px"><h3>Reinforced Concrete, Masonry, &amp; Other</h3><p>Reinforced Concrete Structures, Masonry, Shotcrete, Slab On Grade, Sitework, De Watering, Demolition...</p></div>
  <div class="svc-ico bg-navy" style="left:142px;top:416px"><svg width="30" height="24" viewBox="0 0 30 24" fill="#fff"><rect x="2" y="4" width="26" height="4"/><rect x="2" y="10" width="12" height="4"/><rect x="16" y="10" width="12" height="4"/><rect x="2" y="16" width="26" height="4"/></svg></div>
  <div class="svc right" style="left:616px;top:391px"><h3>Engineering &amp; Design Support</h3><p>Design Review And Support, Structural Monitoring, Engineering &amp; Design, Preconstruction Services...</p></div>
  <div class="svc-ico bg-blue" style="left:1000px;top:416px"><svg width="28" height="28" viewBox="0 0 24 24" fill="#fff"><path d="M4 14a8 8 0 0116 0z"/><rect x="2" y="14" width="20" height="2.5"/><rect x="10.5" y="4" width="3" height="5"/><path d="M7 19h10l-1 2H8z"/></svg></div>
</section>

<section class="why">
  <div class="abs why-edge" role="img" aria-label="Decorative blue edge band"></div>
  <div class="abs why-text">
    <div class="eyebrow">Why Choose Us</div>
    <h2 class="h2">Why Owners, CM's, and<br>GC's <b>Copper Ridge</b></h2>
    <p>Foundation and geotechnical work sets the tone for the project and every phase that follows. Copper Ridge brings a self-performing, safety-first, engineering-informed approach to every market we serve — helping project teams de-risk the ground-level phase of construction through constructability review, value engineering, and disciplined field execution.</p>
    <p>Whether the project calls for helical piles on a residential lot or a full earth-retention and deep-foundation package on a commercial high-rise, Copper Ridge delivers the same standard: precision, accountability, and true partnership from the ground up.</p>
  </div>
  <div class="abs why-photo" role="img" aria-label="Excavated pit lined with timber lagging earth-retention walls"></div>
</section>

<section class="projects">
  <div class="sec-head" style="top:88px">
    <div class="eyebrow center">Our Projects</div>
    <h2 class="h2">Where Strong Foundations<br><b>Become Successful Projects</b></h2>
    <p style="margin-top:6px">Every Project Reflects Our Commitment To Precision, Safety, And Engineering Excellence In Challenging Ground Conditions.</p>
  </div>
  <div class="proj" style="left:140px;top:248px;background:linear-gradient(170deg,#b9c8d6 0%,#9a8663 45%,#6f5a40 100%)" role="img" aria-label="Concrete tower under construction with formwork and rebar">
    <div class="proj-shade"></div><div class="proj-cap"><small>Deep Foundation System</small><strong>Midtown Office Tower</strong></div><div class="proj-arrow"><svg width="14" height="14" viewBox="0 0 14 14"><path d="M3 11L11 3M5 3h6v6" stroke="#fff" stroke-width="1.5" fill="none"/></svg></div>
  </div>
  <div class="proj" style="left:610px;top:248px;background:linear-gradient(170deg,#b8c6d4 0%,#8a5a45 40%,#6b4837 100%)" role="img" aria-label="Brick apartment building with lift platforms">
    <div class="proj-shade"></div><div class="proj-cap"><small>Residential Foundation Work</small><strong>Residential Complex</strong></div><div class="proj-arrow"><svg width="14" height="14" viewBox="0 0 14 14"><path d="M3 11L11 3M5 3h6v6" stroke="#fff" stroke-width="1.5" fill="none"/></svg></div>
  </div>
  <div class="proj" style="left:140px;top:662px;background:linear-gradient(180deg,#9ea3a6 0%,#8c9195 50%,#6d6f70 100%)" role="img" aria-label="Poured concrete foundation walls in an excavation">
    <div class="proj-shade"></div><div class="proj-cap"><small>Industrial Site Development</small><strong>Metro Distribution Center</strong></div><div class="proj-arrow"><svg width="14" height="14" viewBox="0 0 14 14"><path d="M3 11L11 3M5 3h6v6" stroke="#fff" stroke-width="1.5" fill="none"/></svg></div>
  </div>
  <div class="proj" style="left:610px;top:662px;background:linear-gradient(180deg,#a8a8a2 0%,#8f8574 50%,#6e6457 100%)" role="img" aria-label="Deep excavation with concrete walls and shoring">
    <div class="proj-shade"></div><div class="proj-cap"><small>Earth Retention Solutions</small><strong>Infrastructure Project</strong></div><div class="proj-arrow"><svg width="14" height="14" viewBox="0 0 14 14"><path d="M3 11L11 3M5 3h6v6" stroke="#fff" stroke-width="1.5" fill="none"/></svg></div>
  </div>
</section>

<section class="markets">
  <div class="sec-head" style="top:90px">
    <div class="eyebrow center">Markets &amp; Industries</div>
    <h2 class="h2">Built for Complex Ground<br><b>Conditions Across Every Sector</b></h2>
    <p style="margin-top:8px">Copper Ridge Construction Serves Owners, Construction Managers, And General Contractors And Subcontractors<br>Across The New York, New Jersey, And Connecticut Tri-State Region. Our Self-Performing Model Allows Us To Support<br>Projects Of Every Scale And Complexity Throughout The Region.</p>
  </div>
  <div class="mkt" style="left:142px"><div class="mkt-ico"><svg width="22" height="22" viewBox="0 0 24 24" fill="#fff"><path d="M3 21V5h10v16zM14 21V10h7v11z"/></svg></div><h4>Commercial</h4><p>Office, Retail, And Mixed-Use Foundation And Structural Packages</p></div>
  <div class="mkt" style="left:330px"><div class="mkt-ico" style="background:var(--navy)"><svg width="22" height="22" viewBox="0 0 24 24" fill="#fff"><path d="M12 3l9 8h-3v10H6V11H3z"/></svg></div><h4>Residential</h4><p>Multi-Family And Single-Family Foundation, Underpinning, And Earth-Retention Work</p></div>
  <div class="mkt" style="left:518px"><div class="mkt-ico"><svg width="22" height="22" viewBox="0 0 24 24" fill="#fff"><path d="M2 21V11l6 3v-3l6 3v-3l6 3V4h2v17z"/></svg></div><h4>Industrial</h4><p>Warehouse And Distribution Center Foundation Systems, Including Complete Structural Packages</p></div>
  <div class="mkt" style="left:706px"><div class="mkt-ico" style="background:var(--navy)"><svg width="22" height="22" viewBox="0 0 24 24" fill="none" stroke="#fff" stroke-width="2"><circle cx="12" cy="12" r="4"/><path d="M12 3v4M12 17v4M3 12h4M17 12h4"/></svg></div><h4>Public Works &amp; Infrastructure</h4><p>Municipal, Transportation, And Public Agency Projects</p></div>
  <div class="mkt" style="left:894px"><div class="mkt-ico"><svg width="22" height="22" viewBox="0 0 24 24" fill="#fff"><rect x="3" y="4" width="18" height="13" rx="1"/><path d="M9 20h6v-3H9z"/></svg></div><h4>Institutional</h4><p>Healthcare, Education, And Government Facility Foundation Work</p></div>
</section>

<footer class="site-footer">
  <div class="abs cta"></div>
  <div class="abs cta-photo" role="img" aria-label="Construction worker in a hard hat with arms crossed"></div>
  <h2 class="abs cta-title">Let's Build From <b>The Ground<br>Up Together</b></h2>
  <p class="abs cta-sub">Partner With Copper Ridge Construction For Reliable, Engineering-Driven Foundation And Geotechnical Solutions Across Your Next Project.</p>
  <div class="abs cta-btn ghost">Request a Quote</div>
  <div class="abs cta-btn fill">Contact Us</div>

  <div class="abs fcol" style="left:140px"><h5>Quick Links</h5><ul><li>Home</li><li>About Us</li><li>Services</li><li>Portfolio</li><li>Industries</li></ul></div>
  <div class="abs fcol" style="left:332px"><h5>Useful Links</h5><ul><li>Contact Us</li><li>Privacy Policy</li><li>Terms &amp; Condition</li></ul></div>
  <div class="abs fcol" style="left:594px;width:260px"><h5>Contact Details</h5>
    <div class="contact-item"><svg width="14" height="16" viewBox="0 0 24 24" fill="#fff"><path d="M12 2a7 7 0 00-7 7c0 5 7 13 7 13s7-8 7-13a7 7 0 00-7-7zm0 9.5A2.5 2.5 0 1112 6.5a2.5 2.5 0 010 5z"/></svg><span>123, Lorem Ipsum Is Simply Dummy<br>Text Of The Printing &amp; Typesetting</span></div>
    <div class="contact-item"><svg width="14" height="16" viewBox="0 0 24 24" fill="#fff"><path d="M6.6 10.8a15.1 15.1 0 006.6 6.6l2.2-2.2c.3-.3.7-.4 1-.2 1.1.4 2.3.6 3.6.6.6 0 1 .4 1 1V20c0 .6-.4 1-1 1A17 17 0 013 4c0-.6.4-1 1-1h3.5c.6 0 1 .4 1 1 0 1.3.2 2.5.6 3.6.1.3 0 .7-.2 1z"/></svg><span>Phone<br>+1-555-014-2290</span></div>
    <div class="contact-item"><svg width="14" height="16" viewBox="0 0 24 24" fill="#fff"><path d="M2 5h20v14H2zm2 2v.5l8 5 8-5V7z"/></svg><span>Email<br>info@copperridge.com</span></div>
  </div>
  <div class="abs fcol" style="left:955px"><h5>Social Media</h5>
    <ul class="social" style="margin-top:16px"><li><span class="dot on"></span>Socialhub</li><li><span class="dot"></span>Videocast</li><li><span class="dot"></span>Proflink</li><li><span class="dot"></span>Photofeed</li></ul>
  </div>
  <div class="abs foot-rule"></div>
  <div class="abs copyright">Copyright© 2026 Copper Ridge Construction | All Rights Reserved.</div>
</footer>

</body>
</html>
```